Create Premium Wine Label Design

We are premium wine exporters from Australia. We are looking to introduce new brand " The Velloro" - in red wine, White wine and Sparkling wine to international market.

The sample label design for red wine ( Shiraz) is attached.

This is our luxury brand. We need a stunning wine label designs for (front, back and neck) that should be mostly in GOLD colour and design should be really eye catching.

We have provided sample design for front, back and neck labels. However, we are looking forward to see a completely new improvised design.

LOGO attached.

Front Label Design Specification:

* We would like to see designs that are in Gold colour.
* Wine Bottle size is standard: 750ml; we assume the same design can be resizable to different bottle sizes.
* Our design should suit both black, white and sparkling wine bottles(sample attached)
* Use our logo in the design (see attached - label sample)
* Content for front label (see attached).
* Design should include all information specified in the sample

Back Label Design
* All contents in the sample should be used ( sample attached)
* LOGO attached.

Neck Label Design
* Sample of Neck label attached, please provide similar or your own design.
* LOGO attached.

Image Samples:
* Samples of label designs we like (see attached)
* Sample for gold color (see attached)
* For bottle shapes (see attached)
* Front, Back and Neck Label Samples (see attached)

Target Market(s)

International Wine Market

Font styles to use
Decorative
Script

Requirements
Must have
• Must have golden color on front and back label

```html
<!DOCTYPE html>
<html lang="en">
<head>
<meta charset="utf-8">
<title>The Velloro Shiraz – Label Set</title>
<link rel="stylesheet" href="https://fonts.googleapis.com/css2?family=Cinzel:wght@400;600&family=PT+Sans:wght@400;700&display=swap">
<style>
  :root {
    --page: #ffffff;
    --label-dark: #2b2b2b;
    --label-deep: #1f1f1f;
    --logo-box: #3a3a3a;
    --gold-light: #f3dc95;
    --gold: #c9a24a;
    --gold-deep: #8a6a24;
    --pattern-dark: #242424;
    --ink: #111111;
    --white: #f4f1ea;
    --gold-bar: linear-gradient(90deg, var(--gold-deep), var(--gold-light) 45%, var(--gold) 70%, var(--gold-deep));
    --gold-text: linear-gradient(180deg, var(--gold-light), var(--gold) 60%, var(--gold-deep));
  }
  * { margin: 0; padding: 0; box-sizing: border-box; }
  html, body { width: 1200px; height: 1106px; overflow: hidden; background: var(--page); }
  .sheet { position: relative; width: 1200px; height: 1106px; }

  .label { position: absolute; overflow: visible; }
  .gold-type {
    background: var(--gold-text);
    -webkit-background-clip: text; background-clip: text; color: transparent;
  }
  .center { position: absolute; left: 0; right: 0; text-align: center; }

  /* shared pieces */
  .logo-box {
    position: absolute; background: var(--logo-box);
    display: flex; align-items: center; justify-content: center; gap: 6px;
  }
  .logo-box .dot { width: 8px; height: 8px; background: var(--gold); }
  .logo-name {
    font-family: "Cinzel", serif; font-weight: 600; color: var(--gold);
    letter-spacing: 0.5px;
  }
  .crown, .ornament { position: absolute; }
  .crown { background: linear-gradient(180deg, var(--gold-light), var(--gold-deep)); border-radius: 2px; }
  .ornament {
    background: linear-gradient(90deg, transparent, var(--gold) 20%, var(--gold-light) 50%, var(--gold) 80%, transparent);
    opacity: 0.85; border-radius: 50%;
  }
  .wordmark-the { font-family: "Cinzel", serif; font-weight: 400; }
  .wordmark-main { font-family: "Cinzel", serif; font-weight: 400; letter-spacing: -1px; }
  .varietal { font-family: "PT Sans", sans-serif; font-weight: 700; color: var(--white); }

  /* front */
  .front { left: 22px; top: 300px; width: 436px; height: 436px; background: var(--pattern-dark); }
  .front .pattern {
    position: absolute; top: 0; bottom: 0; width: 108px;
    background: repeating-linear-gradient(45deg, #2a2a2a 0 10px, #8d7440 10px 13px, #2a2a2a 13px 22px),
                linear-gradient(var(--pattern-dark), var(--pattern-dark));
  }
  .front .pattern.left { left: 0; }
  .front .pattern.right { right: 0; }
  .front .bar { position: absolute; top: 0; bottom: 0; width: 19px; background: var(--gold-bar); }
  .front .bar.left { left: 108px; }
  .front .bar.right { left: 310px; }
  .front .panel { position: absolute; left: 127px; width: 183px; top: 0; bottom: 0; background: var(--label-dark); }
  .front .logo-box { left: 40px; top: 14px; width: 100px; height: 72px; }
  .front .logo-name { font-size: 12px; }
  .front .crown { left: 80px; top: 106px; width: 24px; height: 20px; }
  .front .wordmark-the { top: 132px; font-size: 24px; }
  .front .wordmark-main { top: 154px; font-size: 38px; line-height: 40px; }
  .front .ornament.top { left: 22px; width: 140px; top: 224px; height: 34px; }
  .front .varietal { top: 262px; font-size: 30px; }
  .front .ornament.bottom { left: 42px; width: 100px; top: 296px; height: 22px; }
  .front .vintage { top: 326px; font-family: "PT Sans", sans-serif; font-weight: 700; font-size: 32px; }
  .front .origin { top: 396px; font-family: "PT Sans", sans-serif; font-size: 11px; color: var(--white); }

  /* back */
  .back { left: 500px; top: 300px; width: 218px; height: 436px;
    background: linear-gradient(180deg, var(--label-dark) 0%, var(--label-dark) 74%, #5b4a24 90%, var(--gold) 100%); }
  .back .edge { position: absolute; top: 0; bottom: 0; width: 12px; background: var(--gold-bar); }
  .back .edge.left { left: 0; }
  .back .edge.right { right: 0; }
  .back .logo-box { left: 58px; top: -22px; width: 98px; height: 72px; }
  .back .logo-name { font-size: 11px; }
  .back .ornament.top { left: 38px; width: 142px; top: 60px; height: 34px; }
  .back .varietal { top: 98px; font-size: 26px; }
  .back .ornament.bottom { left: 58px; width: 102px; top: 128px; height: 22px; }
  .back .crown { left: 99px; top: 160px; width: 20px; height: 15px; }
  .back .wordmark-the { top: 176px; font-size: 18px; }
  .back .wordmark-main { top: 192px; font-size: 29px; line-height: 32px; }
  .back .story {
    top: 252px; left: 20px; right: 20px; font-family: "PT Sans", sans-serif;
    font-size: 9.4px; line-height: 12px; color: var(--white);
  }
  .back .facts {
    position: absolute; right: 24px; top: 376px; width: 100px; text-align: center;
    font-family: "PT Sans", sans-serif; font-size: 6.2px; line-height: 7.6px; color: var(--ink);
  }

  /* neck */
  .neck { left: 750px; top: 398px; width: 434px; height: 66px; background: var(--pattern-dark); }
  .neck .rim { position: absolute; left: 0; right: 0; top: 0; height: 5px; background: var(--gold-bar); }
  .neck .band { position: absolute; left: 0; right: 0; top: 5px; height: 31px; background: var(--label-dark);
    display: flex; align-items: center; justify-content: center; border-bottom: 2px solid var(--gold); }
  .neck .country { font-family: "Cinzel", serif; font-weight: 600; font-size: 16px; letter-spacing: 1px; color: #9a9a9a; }
  .neck .pattern { position: absolute; left: 0; right: 0; top: 36px; bottom: 0;
    background: repeating-linear-gradient(135deg, #2a2a2a 0 9px, #b89a5a 9px 12px, #2a2a2a 12px 20px); }

  /* captions */
  .caption { position: absolute; top: 782px; font-family: "PT Sans", sans-serif; font-size: 34px; color: var(--ink); text-align: center; }
  .caption.front-cap { left: 22px; width: 436px; }
  .caption.back-cap { left: 500px; width: 218px; }
  .caption.neck-cap { left: 750px; width: 434px; }
</style>
</head>
<body>
<main class="sheet">

  <section class="label front" aria-label="Front label">
    <div class="pattern left" role="img" aria-label="Gold interlocking geometric pattern"></div>
    <div class="bar left"></div>
    <div class="panel">
      <div class="logo-box"><span class="dot"></span><span class="logo-name">SOUTHVALE</span></div>
      <div class="crown" role="img" aria-label="Small gold crown ornament"></div>
      <div class="center wordmark-the gold-type">THE</div>
      <div class="center wordmark-main gold-type">VELLORO</div>
      <div class="ornament top" role="img" aria-label="Gold filigree flourish above varietal"></div>
      <div class="center varietal">SHIRAZ</div>
      <div class="ornament bottom" role="img" aria-label="Gold filigree flourish below varietal"></div>
      <div class="center vintage gold-type">2018</div>
      <div class="center origin">Wine of Australia</div>
    </div>
    <div class="bar right"></div>
    <div class="pattern right" role="img" aria-label="Gold interlocking geometric pattern"></div>
  </section>

  <section class="label back" aria-label="Back label">
    <div class="edge left"></div>
    <div class="edge right"></div>
    <div class="logo-box"><span class="dot"></span><span class="logo-name">SOUTHVALE</span></div>
    <div class="ornament top" role="img" aria-label="Gold filigree flourish above varietal"></div>
    <div class="center varietal">SHIRAZ</div>
    <div class="ornament bottom" role="img" aria-label="Gold filigree flourish below varietal"></div>
    <div class="crown" role="img" aria-label="Small gold crown ornament"></div>
    <div class="center wordmark-the gold-type">THE</div>
    <div class="center wordmark-main gold-type">VELLORO</div>
    <p class="center story">Lorem ipsum dolor sit amet, consectetuer adipiscing elit, sed diam nonummy nibh euismod tincidunt ut laoreet dolore magna ali Lorem ipsum dolor sit amet, consectetuer adipiscing elit, sed diam nonummy nibh euismod tincidunt ut laoreet dolore magna ali</p>
    <p class="facts">Product of Australia<br>Presevative (220)<br>Antioxidant (300).<br>May contain traces of milk.<br>Country of origin: Australia.<br>Southvale Estates, PTY. Ltd.<br>Ridgeford, Victoria, Australia</p>
  </section>

  <section class="label neck" aria-label="Neck label">
    <div class="rim"></div>
    <div class="band"><span class="country">AUSTRALIA</span></div>
    <div class="pattern" role="img" aria-label="Gold zigzag geometric pattern"></div>
  </section>

  <p class="caption front-cap">Front</p>
  <p class="caption back-cap">Back</p>
  <p class="caption neck-cap">Neck</p>

</main>
</body>
</html>
```